Business card and stationary for Auto Parts
Vern's Auto Parts
Use same font as used in my logo
Dale Korthauer
Manager
2457 E. 14 Birch Lane
vernsautoparts@kelvomail.com
www.vernsautoparts-demo.com
Store Hours:
Monday-Friday 8am-6pm
Saturday 8am-3pm
add small qv logo

```html
<!DOCTYPE html>
<html lang="en">
<head>
<meta charset="utf-8">
<title>Vern's Auto Parts – Business Card</title>
<link href="https://fonts.googleapis.com/css2?family=Michroma&display=swap" rel="stylesheet">
<style>
  :root {
    --backdrop: #e9e6e2;
    --card: #ffffff;
    --red: #d1222b;
    --red-dark: #8e1016;
    --steel: #b9bcc0;
    --steel-dark: #85898e;
    --ink: #3a3a3c;
    --muted: #77797c;
    --logo-dark: #2b2b2e;
  }
  * { margin: 0; padding: 0; box-sizing: border-box; }
  html, body {
    width: 1200px; height: 914px; overflow: hidden;
    background: var(--backdrop);
    font-family: "Michroma", sans-serif;
    color: var(--ink);
  }
  .card {
    position: absolute; left: 100px; top: 171px;
    width: 1000px; height: 572px;
    background: var(--card);
    box-shadow: 0 12px 30px rgba(0,0,0,.18);
    overflow: hidden;
  }
  .card-bands { position: absolute; inset: 0; }
  .brand {
    position: absolute; left: 0; right: 0; top: 95px;
    display: flex; align-items: center; justify-content: center; gap: 22px;
  }
  .brand-dot {
    width: 46px; height: 46px; border-radius: 50%;
    background: var(--logo-dark);
  }
  .brand-name {
    font-size: 40px; color: var(--logo-dark); letter-spacing: 2px;
    text-transform: uppercase;
  }
  .holder {
    position: absolute; right: 545px; top: 282px; text-align: right;
  }
  .holder-name {
    font-size: 19px; color: var(--red); letter-spacing: 2px;
    text-transform: uppercase;
  }
  .holder-role {
    margin-top: 8px; font-size: 15px; color: var(--muted);
    letter-spacing: 2px; text-transform: uppercase;
  }
  .address {
    position: absolute; right: 545px; top: 405px;
    font-size: 17px; letter-spacing: 2px; color: var(--ink);
  }
  .contacts {
    position: absolute; left: 488px; top: 316px;
    list-style: none;
  }
  .contact {
    display: flex; align-items: center; gap: 14px;
    height: 33px; font-size: 16px; letter-spacing: 2px; color: var(--ink);
  }
  .contact-icon { width: 20px; height: 20px; flex: none; }
</style>
</head>
<body>
  <div class="card">
    <svg class="card-bands" width="1000" height="572" viewBox="0 0 1000 572" aria-hidden="true">
      <defs>
        <linearGradient id="redBand" x1="0" y1="0" x2="1" y2="0">
          <stop offset="0" stop-color="#d1222b"/>
          <stop offset=".55" stop-color="#c51b23"/>
          <stop offset="1" stop-color="#8e1016"/>
        </linearGradient>
        <linearGradient id="steelBand" x1="0" y1="0" x2="1" y2="0">
          <stop offset="0" stop-color="#85898e"/>
          <stop offset=".3" stop-color="#cfd1d4"/>
          <stop offset="1" stop-color="#aeb1b5"/>
        </linearGradient>
      </defs>
      <polygon points="0,355 470,355 440,392 0,392" fill="url(#redBand)"/>
      <polygon points="0,392 440,392 434,400 0,400" fill="#e3e4e6"/>
      <polygon points="478,468 1000,468 1000,500 452,500" fill="url(#steelBand)"/>
      <polygon points="478,468 540,468 514,500 452,500" fill="#d1222b"/>
    </svg>

    <div class="brand">
      <span class="brand-dot"></span>
      <span class="brand-name">Vern's Auto Parts</span>
    </div>

    <div class="holder">
      <p class="holder-name">Dale Korthauer</p>
      <p class="holder-role">Manager</p>
    </div>

    <p class="address">2457 E. 14 Birch Lane</p>

    <ul class="contacts">
      <li class="contact">
        <svg class="contact-icon" viewBox="0 0 20 20" aria-hidden="true"><circle cx="10" cy="10" r="10" fill="#d1222b"/><path d="M7 5.5l1.6 2.2-1 1.1a6 6 0 0 0 3.6 3.6l1.1-1 2.2 1.6-.8 1.6C10 14.4 5.6 10 5.4 6.3z" fill="#fff"/></svg>
        (555)010-2846
      </li>
      <li class="contact">
        <svg class="contact-icon" viewBox="0 0 20 20" aria-hidden="true"><circle cx="10" cy="10" r="10" fill="#d1222b"/><rect x="5" y="6" width="10" height="8" rx="1" fill="#fff"/><rect x="7" y="8" width="6" height="2" fill="#d1222b"/></svg>
        (555)010-2871
      </li>
      <li class="contact">
        <svg class="contact-icon" viewBox="0 0 20 20" aria-hidden="true"><circle cx="10" cy="10" r="10" fill="#d1222b"/><rect x="5" y="6.5" width="10" height="7" fill="#fff"/><path d="M5 6.5l5 4 5-4" fill="none" stroke="#d1222b" stroke-width="1.2"/></svg>
        vernsautoparts@kelvomail.com
      </li>
      <li class="contact">
        <svg class="contact-icon" viewBox="0 0 20 20" aria-hidden="true"><circle cx="10" cy="10" r="10" fill="#d1222b"/><circle cx="10" cy="10" r="5" fill="none" stroke="#fff" stroke-width="1.3"/><path d="M5 10h10M10 5c-2.5 3-2.5 7 0 10M10 5c2.5 3 2.5 7 0 10" fill="none" stroke="#fff" stroke-width="1"/></svg>
        www.vernsautoparts-demo.com
      </li>
    </ul>
  </div>
</body>
</html>
```